Custom Monogramming and Retail gifts

We need a Business Card for a monogramming business that offers many retail gift options. We are a home based business that uses social media (Chatterbox,clipboardia and our website) to sell our products. Our target market is college age, high school, baby gifts.
We want a preppy fun look. Monogramming is very popular in the South

Industry/Entity Type

College

Contact Information for Business Card

Threadwell Keepsakes
Custom Monogramming and Gifts
7152 Brackenway Lane
Gainesville, GA 30999
Della Marsh, Owner
555-314-2790
threadwellkeepsakes.example
threadwellkeepsakes@mailbox.example

```html
<!DOCTYPE html>
<html lang="en">
<head>
<meta charset="utf-8">
<title>Threadwell Keepsakes – Business Card</title>
<link rel="stylesheet" href="https://fonts.googleapis.com/css2?family=Lato:wght@300;400&family=Pinyon+Script&display=swap">
<style>
  :root {
    --backdrop: #d9d9d9;
    --pink-light: #f26fa6;
    --pink: #ea3f8a;
    --pink-deep: #d81f72;
    --white: #ffffff;
  }
  html, body {
    margin: 0;
    width: 1200px;
    height: 900px;
    overflow: hidden;
    background: var(--backdrop);
  }
  .business-card {
    position: absolute;
    left: 100px;
    top: 165px;
    width: 1000px;
    height: 570px;
    border-radius: 34px;
    background: radial-gradient(ellipse at 50% 45%, var(--pink-light) 0%, var(--pink) 55%, var(--pink-deep) 100%);
    box-shadow: 0 10px 30px rgba(0,0,0,0.25);
    color: var(--white);
    font-family: 'Lato', sans-serif;
  }
  .stitch-border {
    position: absolute;
    inset: 18px;
    border: 2px dashed var(--white);
    border-radius: 22px;
  }
  .brand {
    position: absolute;
    top: 70px;
    left: 0;
    right: 0;
    text-align: center;
  }
  .brand-name {
    font-family: 'Lato', sans-serif;
    font-weight: 400;
    font-size: 64px;
    letter-spacing: 1px;
    color: var(--white);
    margin: 0;
  }
  .brand-tagline {
    margin: 26px 0 0;
    font-family: 'Pinyon Script', cursive;
    font-size: 40px;
    line-height: 1.1;
  }
  .brand-tagline .and-gifts {
    display: block;
    font-size: 30px;
    margin-left: 220px;
  }
  .owner {
    position: absolute;
    left: 70px;
    top: 380px;
    font-family: 'Pinyon Script', cursive;
  }
  .owner-name {
    font-size: 62px;
    margin: 0;
    line-height: 1;
  }
  .owner-title {
    font-size: 42px;
    margin: -6px 0 0 40px;
    line-height: 1;
  }
  .contact {
    position: absolute;
    left: 530px;
    top: 360px;
    width: 410px;
    font-weight: 300;
    font-size: 19px;
  }
  .contact-list {
    list-style: none;
    margin: 0;
    padding: 0 0 10px;
    border-bottom: 2px dotted var(--white);
  }
  .contact-list li {
    display: flex;
    align-items: center;
    height: 32px;
  }
  .contact-icon {
    width: 22px;
    height: 22px;
    margin-right: 14px;
    flex: none;
  }
  .address {
    margin: 12px 0 0;
  }
</style>
</head>
<body>
  <article class="business-card">
    <div class="stitch-border"></div>

    <header class="brand">
      <h1 class="brand-name">Threadwell Keepsakes</h1>
      <p class="brand-tagline">Custom Monogramming<span class="and-gifts">and Gifts</span></p>
    </header>

    <div class="owner">
      <p class="owner-name">Della Marsh</p>
      <p class="owner-title">owner</p>
    </div>

    <div class="contact">
      <ul class="contact-list">
        <li>
          <svg class="contact-icon" viewBox="0 0 24 24" aria-hidden="true"><path fill="#fff" d="M6.6 10.8c1.4 2.8 3.8 5.1 6.6 6.6l2.2-2.2c.3-.3.7-.4 1-.2 1.1.4 2.3.6 3.6.6.6 0 1 .4 1 1V20c0 .6-.4 1-1 1C10.6 21 3 13.4 3 4c0-.6.4-1 1-1h3.5c.6 0 1 .4 1 1 0 1.3.2 2.5.6 3.6.1.3 0 .7-.2 1l-2.3 2.2z"/></svg>
          <span>: 555-314-2790</span>
        </li>
        <li>
          <svg class="contact-icon" viewBox="0 0 24 24" aria-hidden="true"><rect x="2" y="5" width="20" height="14" fill="none" stroke="#fff" stroke-width="1.6"/><path d="M2 5l10 8 10-8" fill="none" stroke="#fff" stroke-width="1.6"/></svg>
          <span>: threadwellkeepsakes@mailbox.example</span>
        </li>
        <li>
          <svg class="contact-icon" viewBox="0 0 24 24" aria-hidden="true"><g fill="none" stroke="#fff" stroke-width="1.5"><circle cx="12" cy="12" r="9"/><ellipse cx="12" cy="12" rx="4" ry="9"/><path d="M3 12h18M5 7h14M5 17h14"/></g></svg>
          <span>: threadwellkeepsakes.example</span>
        </li>
      </ul>
      <p class="address">7152 Brackenway Lane Gainesville, GA 30999</p>
    </div>
  </article>
</body>
</html>
```